Laundry pickup and delivery flyer "Fold Harbor laundry"

I need a flyer "8.5"x11" that tells customers about our pickup and delivery laundry service. our website address is: www.foldharborlaundry.example The flyer should be front and back.

Font styles to use
Sans Serif

Colors
0094D4
00A9DD
6FCCEA
C7EBF8
E9F6FB

```html
<!DOCTYPE html>
<html lang="en">
<head>
<meta charset="utf-8">
<title>Fold Harbor laundry – Pickup &amp; Delivery</title>
<link rel="stylesheet" href="https://fonts.googleapis.com/css2?family=Ubuntu:wght@400;500;700&display=swap">
<style>
  :root {
    --sky: #e2fbfd;
    --stripe: #c7f3f8;
    --stripe-deep: #8fe6ef;
    --frame: #2fdfea;
    --panel: #ffffff;
    --bubble: #56d3d6;
    --ink: #111111;
    --brand: #1f7ee6;
    --van-blue: #2a7fe0;
    --van-light: #c7ebf8;
  }
  * { margin: 0; padding: 0; box-sizing: border-box; }
  html, body { width: 849px; height: 1200px; overflow: hidden; }
  body { font-family: "Ubuntu", sans-serif; color: var(--ink); background: var(--sky); }
  .flyer { position: relative; width: 849px; height: 1200px; overflow: hidden; background: var(--sky); }
  .backdrop { position: absolute; inset: 0; }
  .brand-name {
    position: absolute; left: 0; width: 849px; top: 100px;
    text-align: center; font-weight: 700; font-size: 46px; letter-spacing: 1px;
    color: var(--brand);
  }
  .brand-name .dot {
    display: inline-block; width: 18px; height: 18px; border-radius: 50%;
    background: var(--brand); margin-right: 12px; vertical-align: 6px;
  }
  .section-title {
    position: absolute; left: 0; width: 849px; text-align: center; font-weight: 700;
  }
  .how-title { top: 234px; font-size: 48px; font-weight: 500; }
  .why-title { top: 564px; font-size: 52px; letter-spacing: 1px; }
  .steps { position: absolute; top: 300px; left: 0; width: 849px; height: 260px; }
  .step { position: absolute; top: 0; width: 162px; }
  .step-icon {
    width: 154px; height: 154px; border-radius: 50%; background: var(--bubble);
    margin-left: 4px; display: flex; align-items: center; justify-content: center;
  }
  .step-text {
    margin-top: 26px; font-size: 16px; line-height: 19.3px;
    text-align: justify; text-align-last: left; letter-spacing: 0.6px;
  }
  .step-1 { left: 47px; } .step-2 { left: 244px; }
  .step-3 { left: 442px; } .step-4 { left: 639px; }
  .why-list {
    position: absolute; top: 620px; left: 0; width: 849px; text-align: center;
    font-size: 16.5px; line-height: 19.6px; list-style: none;
  }
  .van-photo {
    position: absolute; left: 74px; top: 912px; width: 722px; height: 278px;
    border-radius: 40px 60px 30px 30px;
    background: linear-gradient(90deg, var(--van-blue) 0%, var(--van-blue) 30%, #ffffff 42%, #ffffff 70%, var(--van-light) 82%, var(--van-blue) 100%);
  }
</style>
</head>
<body>
<main class="flyer">
  <svg class="backdrop" width="849" height="1200" viewBox="0 0 849 1200" aria-hidden="true">
    <g fill="var(--stripe)">
      <polygon points="0,40 60,0 120,0 0,120"/>
      <polygon points="0,250 140,90 170,120 0,330"/>
      <polygon points="0,560 150,380 170,420 0,640"/>
      <polygon points="0,860 160,640 180,690 0,940"/>
      <polygon points="849,40 789,0 729,0 849,120"/>
      <polygon points="849,250 709,90 679,120 849,330"/>
      <polygon points="849,560 699,380 679,420 849,640"/>
      <polygon points="849,860 689,640 669,690 849,940"/>
    </g>
    <g fill="var(--stripe-deep)" opacity="0.55">
      <polygon points="0,160 40,120 50,135 0,190"/>
      <polygon points="849,160 809,120 799,135 849,190"/>
      <polygon points="0,700 60,620 70,640 0,730"/>
      <polygon points="849,700 789,620 779,640 849,730"/>
    </g>
    <path class="top-panel" d="M110,-6 L175,150 Q205,216 275,216 L575,216 Q645,216 675,150 L740,-6 Z"
          fill="var(--panel)" stroke="var(--frame)" stroke-width="6"/>
    <path class="bottom-panel" d="M28,1206 L28,985 Q28,935 75,910 L380,735 Q424,712 468,735 L775,910 Q822,935 822,985 L822,1206 Z"
          fill="var(--panel)" stroke="var(--frame)" stroke-width="8"/>
  </svg>

  <div class="brand-name"><span class="dot"></span>FOLD HARBOR</div>

  <h1 class="section-title how-title">How It Works!</h1>

  <section class="steps">
    <div class="step step-1">
      <div class="step-icon">
        <svg width="104" height="104" viewBox="0 0 104 104" aria-hidden="true" fill="none" stroke="#fff" stroke-linecap="round">
          <circle cx="52" cy="52" r="48" stroke-width="5"/>
          <g stroke-width="4">
            <line x1="52" y1="12" x2="52" y2="19"/><line x1="52" y1="85" x2="52" y2="92"/>
            <line x1="12" y1="52" x2="19" y2="52"/><line x1="85" y1="52" x2="92" y2="52"/>
            <line x1="24" y1="24" x2="28" y2="28"/><line x1="80" y1="24" x2="76" y2="28"/>
            <line x1="24" y1="80" x2="28" y2="76"/><line x1="80" y1="80" x2="76" y2="76"/>
          </g>
          <polyline points="28,36 52,54 80,36" stroke-width="5"/>
        </svg>
      </div>
      <p class="step-text">feel free to leave your bag where our driver can get to it.</p>
    </div>
    <div class="step step-2">
      <div class="step-icon">
        <svg width="120" height="80" viewBox="0 0 120 80" aria-hidden="true" fill="none" stroke="#fff" stroke-width="4" stroke-linejoin="round">
          <path d="M4,58 L4,38 L28,12 Q31,8 37,8 L110,8 Q116,8 116,14 L116,50 Q116,58 110,58 L90,58 M66,58 L38,58 M16,58 L4,58"/>
          <path d="M28,34 L40,18 L58,18 L58,34 Z"/>
          <circle cx="27" cy="58" r="9"/><circle cx="78" cy="58" r="9"/>
          <line x1="14" y1="76" x2="106" y2="76"/>
        </svg>
      </div>
      <p class="step-text">Our driver will pickup your clothes at the scheduled time.</p>
    </div>
    <div class="step step-3">
      <div class="step-icon">
        <svg width="80" height="96" viewBox="0 0 80 96" aria-hidden="true">
          <rect x="0" y="0" width="80" height="96" rx="5" fill="#fff"/>
          <rect x="0" y="14" width="80" height="3" fill="var(--bubble)"/>
          <circle cx="10" cy="7" r="3" fill="var(--bubble)"/><circle cx="20" cy="7" r="3" fill="var(--bubble)"/>
          <rect x="48" y="4" width="24" height="6" rx="3" fill="var(--bubble)"/>
          <circle cx="40" cy="56" r="30" fill="var(--bubble)"/>
          <circle cx="40" cy="56" r="25" fill="#fff"/>
          <path d="M15,60 Q21,55 27,60 Q33,65 40,60 Q47,55 53,60 Q59,65 65,60 A25,25 0 0 1 15,60 Z" fill="var(--bubble)"/>
        </svg>
      </div>
      <p class="step-text">Your clothes are expertly cleaned by our team of professionals</p>
    </div>
    <div class="step step-4">
      <div class="step-icon">
        <svg width="104" height="100" viewBox="0 0 104 100" aria-hidden="true" fill="none" stroke="#fff" stroke-width="5" stroke-linecap="round" stroke-linejoin="round">
          <path d="M46,14 Q46,4 52,4 Q58,4 58,11 Q58,18 52,21 L52,28"/>
          <path d="M52,28 L6,60 Q2,66 8,66 L96,66 Q102,66 98,60 Z"/>
          <rect x="18" y="62" width="58" height="30" fill="#fff" stroke="none"/>
          <line x1="82" y1="62" x2="82" y2="92"/>
        </svg>
      </div>
      <p class="step-text">We delivery your clean clothes back to you at your convenience!</p>
    </div>
  </section>

  <h2 class="section-title why-title">WHY FOLD HARBOR?</h2>
  <ul class="why-list">
    <li>Our laundry professionals separate lights and darks to keep your clothes looking great!</li>
    <li>Your items will never be washed with anyone else’s</li>
    <li>We use high quality detergents and eco friends chemicals</li>
    <li>No more Laundry day!</li>
  </ul>

  <div class="van-photo" role="img" aria-label="Photo of the branded blue and white Fold Harbor pickup and delivery van, side view"></div>
</main>
</body>
</html>
```